Men's and Boys sports themed barbershop. I was wanting to see what a black card would look like. I think white is too plain, but I am just needing some ideas for a design or background.

Contact Information for Business Card

Ace Trims
4826 E. Harbor Pine Rd
Bayview Springs, Ga 34512
(555) 555-0142
ace_trims@quellmail.com
Denise Marlow (on one side) Gregory Marlow (on opposite side)
Owner
(555) 555-0187 (Denise) (555) 555-0163

```html
<!DOCTYPE html>
<html lang="en">
<head>
<meta charset="utf-8">
<title>Ace Trims — Business Cards</title>
<link rel="stylesheet" href="https://fonts.googleapis.com/css2?family=Questrial&display=swap">
<style>
  :root {
    --backdrop: #2e2e2e;
    --card: #131313;
    --card-edge: #1c1c1c;
    --ink-strong: #6a6a6a;
    --ink: #5a5a5a;
    --ink-soft: #515151;
  }
  * { margin: 0; padding: 0; box-sizing: border-box; }
  html, body {
    width: 1200px;
    height: 819px;
    overflow: hidden;
    background: var(--backdrop);
    font-family: "Questrial", "Century Gothic", sans-serif;
  }
  .sheet {
    position: relative;
    width: 1200px;
    height: 819px;
    display: flex;
    align-items: center;
    justify-content: center;
    gap: 40px;
  }
  .card {
    position: relative;
    width: 540px;
    height: 309px;
    background: var(--card);
    border: 1px solid var(--card-edge);
    border-radius: 3px;
    box-shadow: 0 18px 40px rgba(0,0,0,0.45);
    color: var(--ink);
  }
  .brand {
    position: absolute;
    display: flex;
    align-items: center;
    gap: 12px;
    color: var(--ink-strong);
    font-size: 40px;
    letter-spacing: 0.5px;
    white-space: nowrap;
  }
  .brand-dot {
    width: 14px;
    height: 14px;
    border-radius: 50%;
    background: var(--ink-strong);
  }
  .card--denise .brand { top: 44px; left: 44px; }
  .card--gregory .brand { top: 70px; right: 44px; }

  .details {
    position: absolute;
    font-size: 11.5px;
    line-height: 1.55;
    color: var(--ink-soft);
    white-space: nowrap;
  }
  .card--denise .details { right: 36px; bottom: 44px; text-align: right; }
  .card--gregory .details { left: 36px; bottom: 52px; text-align: left; }

  .person {
    font-size: 15px;
    letter-spacing: 1.2px;
    text-transform: uppercase;
    color: var(--ink-strong);
    margin-bottom: 12px;
  }
  .role {
    text-transform: none;
    letter-spacing: 0.3px;
    color: var(--ink);
  }
  .label { color: var(--ink); }
</style>
</head>
<body>
  <main class="sheet">
    <section class="card card--denise" aria-label="Business card for Denise Marlow">
      <div class="brand"><span class="brand-dot"></span><span class="brand-name">Ace Trims</span></div>
      <div class="details">
        <p class="person">Denise Marlow</p>
        <p class="contact"><span class="label">T:</span> (555) 555-0163 · <span class="label">M:</span> (555) 555-0187 · <span class="label">E:</span> ace_trims@quellmail.com</p>
        <p class="address">4826 E. Harbor Pine Rd Bayview Springs, Ga 34512</p>
      </div>
    </section>

    <section class="card card--gregory" aria-label="Business card for Gregory Marlow">
      <div class="brand"><span class="brand-dot"></span><span class="brand-name">Ace Trims</span></div>
      <div class="details">
        <p class="person">Gregory Marlow <span class="role">· Owner</span></p>
        <p class="contact"><span class="label">T:</span> (555) 555-0142 · <span class="label">M:</span> (555) 555-0187 · <span class="label">E:</span> ace_trims@quellmail.com</p>
        <p class="address">4826 E. Harbor Pine Rd Bayview Springs, Ga 34512</p>
      </div>
    </section>
  </main>
</body>
</html>
```